Biz Card for Marla Dempsey Insurance Agency
Biz Card for Marla Dempsey Insurance Agency - Financial Services
Creative Brief
Bright & Fun-filled
Marla Dempsey
Independent Agent
Clemmons, NC
office 336-521-0974
cell 336-597-2160
marladempsey34@qorvinmail.com
please include her picture in her new card. I will also upload a copy of what we are currently using. she needs something new and fresh. please use the new logo we upload.
Also, please see the words we are using for the back of her card, please use those same words on the new cards.

```html
<!DOCTYPE html>
<html lang="en">
<head>
<meta charset="utf-8">
<title>Marla Dempsey Insurance Agency – Stationery</title>
<link rel="stylesheet" href="https://fonts.googleapis.com/css2?family=Cinzel:wght@400;700&family=Open+Sans:wght@400;600;700&display=swap">
<style>
:root{
  --stage:#3b3c3e;
  --stage-edge:#2a2b2c;
  --navy:#1d3f73;
  --navy-dark:#163259;
  --green:#3aa34a;
  --green-light:#7cc36b;
  --paper:#ffffff;
  --paper-shade:#eef0f2;
  --ink:#1d3f73;
  --muted:#6d7480;
  --photo:#9a8f86;
}
*{box-sizing:border-box;margin:0;padding:0}
html,body{width:1200px;height:382px;overflow:hidden}
body{
  background:radial-gradient(ellipse at 50% 40%,var(--stage) 0%,var(--stage-edge) 100%);
  font-family:"Open Sans",sans-serif;position:relative;
}
.piece{position:absolute;box-shadow:0 2px 6px rgba(0,0,0,.45)}

/* identity block */
.identity{position:absolute;left:18px;top:20px;width:150px;text-align:center}
.identity-mark{width:62px;height:62px;border-radius:50%;background:var(--paper);margin:0 auto 6px}
.identity-name{font-family:"Cinzel",serif;font-weight:700;font-size:16px;color:var(--paper);letter-spacing:.5px;line-height:1.1}
.identity-sub{font-family:"Cinzel",serif;font-size:8px;color:var(--paper);letter-spacing:1.5px;margin-top:2px}
.identity-label{font-size:8px;color:#c9ccd0;margin-top:3px}

/* cards */
.card{width:112px;height:72px;background:var(--paper);overflow:hidden}
.card .wave{position:absolute;left:0;bottom:0;width:100%;height:22px}
.card-back{padding:7px 8px}
.card-back .tagline{font-size:6px;font-weight:700;color:var(--navy);margin-bottom:3px}
.card-back ul{list-style:none}
.card-back li{font-size:5.5px;color:var(--navy);line-height:8px}
.card-back li::before{content:"";display:inline-block;width:3px;height:3px;border-radius:50%;background:var(--green);margin-right:3px;vertical-align:middle}
.card-back.is-navy{background:var(--navy)}
.card-back.is-navy .tagline,.card-back.is-navy li{color:var(--paper)}
.card-front .brand{position:absolute;left:8px;right:6px;top:5px;white-space:nowrap}
.card-front .brand-name{font-family:"Cinzel",serif;font-weight:700;font-size:6px;line-height:7px;color:var(--navy)}
.card-front .brand-sub{font-family:"Cinzel",serif;font-size:3.6px;line-height:5px;letter-spacing:.8px;color:var(--green)}
.card-front .photo{position:absolute;left:8px;top:20px;width:22px;height:26px;background:linear-gradient(160deg,#b7aca2,var(--photo))}
.card-front .details{position:absolute;left:35px;top:19px;right:4px}
.card-front .person{font-family:"Cinzel",serif;font-weight:700;font-size:7px;line-height:9px;color:var(--navy)}
.card-front .role{font-size:5px;line-height:7px;color:var(--green);font-weight:600;margin-bottom:1px}
.card-front .line{font-size:4.6px;color:var(--muted);line-height:6px;white-space:nowrap}

/* letterheads */
.letterhead{width:196px;height:346px;background:linear-gradient(180deg,var(--paper),var(--paper-shade));top:19px;overflow:hidden}
.letterhead .head{position:absolute;left:0;right:0;top:16px;text-align:center}
.letterhead .head-mark{width:16px;height:16px;border-radius:50%;background:var(--green);margin:0 auto 3px}
.letterhead .head-name{font-family:"Cinzel",serif;font-weight:700;font-size:8px;color:var(--navy)}
.letterhead .head-sub{font-family:"Cinzel",serif;font-size:4.5px;color:var(--green);letter-spacing:1px}
.letterhead .wave{position:absolute;left:0;bottom:0;width:100%;height:78px}
.letterhead .footer{position:absolute;left:0;right:0;bottom:6px;text-align:center;font-size:4.5px;color:var(--paper)}

/* envelopes */
.envelope{width:340px;height:76px;left:848px;background:var(--paper);overflow:hidden}
.envelope svg.flap{position:absolute;inset:0;width:100%;height:100%}
.envelope .env-mark{position:absolute;top:10px;left:50%;margin-left:-9px;width:18px;height:18px;border-radius:50%;background:var(--paper)}
.envelope .return{position:absolute;left:10px;top:8px}
.envelope .return-name{font-family:"Cinzel",serif;font-weight:700;font-size:7px;color:var(--navy)}
.envelope .return-line{font-size:4.5px;color:var(--muted)}
</style>
</head>
<body>

<section class="identity">
  <div class="identity-mark"></div>
  <div class="identity-name">MARLA DEMPSEY</div>
  <div class="identity-sub">INSURANCE AGENCY</div>
  <div class="identity-label">Stationery Example</div>
</section>

<!-- card row 1 -->
<div class="piece card card-back" style="left:12px;top:150px">
  <p class="tagline">Protecting what matters most</p>
  <ul>
    <li>Auto Insurance</li>
    <li>Home Insurance</li>
    <li>Life Insurance</li>
    <li>Business Coverage</li>
    <li>Health Plans</li>
  </ul>
  <svg class="wave" viewBox="0 0 112 22" preserveAspectRatio="none"><path d="M0 16 Q40 4 112 12 V22 H0Z" fill="var(--green)"/><path d="M0 19 Q50 9 112 16 V22 H0Z" fill="var(--navy)"/></svg>
</div>
<div class="piece card card-front" style="left:128px;top:150px">
  <div class="brand">
    <div class="brand-name">Marla Dempsey</div>
    <div class="brand-sub">INSURANCE AGENCY</div>
  </div>
  <div class="photo" role="img" aria-label="Portrait photo of the agent"></div>
  <div class="details">
    <div class="person">Marla Dempsey</div>
    <div class="role">Independent Agent</div>
    <div class="line">office 336-521-0974</div>
    <div class="line">cell 336-597-2160</div>
    <div class="line">marladempsey34@qorvinmail.com</div>
  </div>
  <svg class="wave" viewBox="0 0 112 22" preserveAspectRatio="none"><path d="M0 16 Q60 6 112 14 V22 H0Z" fill="var(--green)"/><path d="M0 19 Q60 10 112 17 V22 H0Z" fill="var(--navy)"/></svg>
</div>

<!-- card row 2 -->
<div class="piece card card-back is-navy" style="left:12px;top:244px">
  <p class="tagline">Auto Home Life Business Health</p>
  <ul>
    <li>Call for a free quote</li>
    <li>Clemmons, NC</li>
    <li>336-521-0974</li>
  </ul>
  <svg class="wave" viewBox="0 0 112 22" preserveAspectRatio="none"><path d="M0 18 Q50 10 112 16 V22 H0Z" fill="var(--green)"/></svg>
</div>
<div class="piece card card-front" style="left:128px;top:244px">
  <div class="brand">
    <div class="brand-name">Marla Dempsey</div>
    <div class="brand-sub">INSURANCE AGENCY</div>
  </div>
  <div class="photo" role="img" aria-label="Portrait photo of the agent"></div>
  <div class="details">
    <div class="person">Marla Dempsey</div>
    <div class="role">Independent Agent</div>
    <div class="line">office 336-521-0974</div>
    <div class="line">cell 336-597-2160</div>
    <div class="line">marladempsey34@qorvinmail.com</div>
  </div>
  <svg class="wave" viewBox="0 0 112 22" preserveAspectRatio="none"><path d="M0 17 Q60 8 112 15 V22 H0Z" fill="var(--navy)"/></svg>
</div>

<!-- letterheads -->
<div class="piece letterhead" style="left:413px">
  <div class="head">
    <div class="head-mark"></div>
    <div class="head-name">Marla Dempsey</div>
    <div class="head-sub">INSURANCE AGENCY</div>
  </div>
  <svg class="wave" viewBox="0 0 196 78" preserveAspectRatio="none">
    <path d="M0 40 Q70 10 196 30 V78 H0Z" fill="var(--green)"/>
    <path d="M0 48 Q80 22 196 40 V78 H0Z" fill="var(--navy)"/>
  </svg>
  <div class="footer">336-521-0974 · marladempsey34@qorvinmail.com · Clemmons, NC</div>
</div>
<div class="piece letterhead" style="left:630px">
  <div class="head">
    <div class="head-mark"></div>
    <div class="head-name">Marla Dempsey</div>
    <div class="head-sub">INSURANCE AGENCY</div>
  </div>
  <svg class="wave" viewBox="0 0 196 78" preserveAspectRatio="none">
    <path d="M0 36 Q90 8 196 34 V78 H0Z" fill="var(--green-light)"/>
    <path d="M0 44 Q90 18 196 42 V78 H0Z" fill="var(--green)"/>
    <path d="M0 52 Q90 28 196 50 V78 H0Z" fill="var(--navy)"/>
  </svg>
  <div class="footer">336-521-0974 · marladempsey34@qorvinmail.com · Clemmons, NC</div>
</div>

<!-- envelopes -->
<div class="piece envelope" style="top:24px">
  <svg class="flap" viewBox="0 0 340 76" preserveAspectRatio="none"><path d="M0 0 H340 V22 Q170 52 0 22Z" fill="var(--green)"/></svg>
  <div class="env-mark"></div>
</div>
<div class="piece envelope" style="top:110px">
  <svg class="flap" viewBox="0 0 340 76" preserveAspectRatio="none"><path d="M0 0 H340 V24 Q170 54 0 24Z" fill="var(--navy)"/></svg>
  <div class="env-mark"></div>
</div>
<div class="piece envelope" style="top:198px">
  <svg class="flap" viewBox="0 0 340 76" preserveAspectRatio="none"><path d="M0 0 L170 40 L340 0" fill="none" stroke="#d9dde2" stroke-width="1"/></svg>
  <div class="return">
    <div class="return-name">Marla Dempsey Insurance Agency</div>
    <div class="return-line">Clemmons, NC · 336-521-0974</div>
  </div>
</div>
<div class="piece envelope" style="top:284px">
  <svg class="flap" viewBox="0 0 340 76" preserveAspectRatio="none"><path d="M0 0 L170 40 L340 0" fill="none" stroke="#d9dde2" stroke-width="1"/><path d="M0 66 Q170 56 340 66 V76 H0Z" fill="var(--navy)"/></svg>
  <div class="return">
    <div class="return-name">Marla Dempsey Insurance Agency</div>
    <div class="return-line">Clemmons, NC · 336-521-0974</div>
  </div>
</div>

</body>
</html>
```